Harbor Light Wellness and Advising, LLC

We need a business card and stationary designed for a new therapy practice for Marcia Tolland. Marcia Tolland is a Therapist who specializes in Therapy for children dealing with trauma and/or stress. Below are some of her thoughts:
colors can include purple, blue, turquoise and green (does NOT have to be all colors) See attached Logos
Marcia Tolland, LMHC
Harbor Light Wellness & Wellness Inc.
4823 W. Quarry Boulevard
Suite 517
Boca Raton, FL 33412
Phone: 561-730-2254
Fax: 561-730-2255
Email: marcia@harborlightwa.example
Website: www.harborlightwa.example

```html
<!DOCTYPE html>
<html lang="en">
<head>
<meta charset="utf-8">
<title>Harbor Light Wellness and Advising – Business Card</title>
<link rel="stylesheet" href="https://fonts.googleapis.com/css2?family=Open+Sans:wght@400;600;700&display=swap">
<style>
  :root {
    --backdrop: #8c969e;
    --leaf-green: #84b126;
    --berry: #8a0047;
    --slate-text: #545a62;
    --paper: #ffffff;
  }
  * { margin: 0; padding: 0; box-sizing: border-box; }
  html, body {
    width: 1200px; height: 1000px; overflow: hidden;
    background: var(--backdrop);
    font-family: "Open Sans", Arial, sans-serif;
  }
  .card {
    position: absolute; left: 75px; top: 200px;
    width: 1050px; height: 600px;
    background: var(--paper);
    box-shadow: 0 10px 30px rgba(0,0,0,0.25);
    overflow: hidden;
  }
  .contact-panel {
    position: absolute; left: 0; top: 0;
    width: 560px; height: 600px;
    background: var(--leaf-green);
    color: var(--slate-text);
  }
  .edge-tab {
    position: absolute; left: 0; width: 14px;
    background: var(--berry);
  }
  .edge-tab--upper { top: 118px; height: 48px; }
  .edge-tab--lower { top: 392px; height: 98px; }
  .holder-name {
    position: absolute; left: 50px; top: 78px;
    font-size: 34px; font-weight: 700; letter-spacing: 0.2px;
  }
  .holder-company {
    position: absolute; left: 50px; top: 126px;
    font-size: 22px; font-weight: 400;
  }
  .contact-list {
    position: absolute; left: 50px; top: 382px;
    list-style: none;
    font-size: 25px; line-height: 42px; font-weight: 400;
  }
  .brand-area {
    position: absolute; left: 560px; top: 0;
    width: 490px; height: 420px;
    display: flex; align-items: center; justify-content: center;
    flex-direction: column; gap: 14px;
  }
  .brand-mark {
    width: 60px; height: 60px; border-radius: 50%;
    background: var(--leaf-green);
  }
  .brand-name {
    font-size: 52px; font-weight: 600; color: var(--leaf-green);
    line-height: 1;
  }
  .address-band {
    position: absolute; left: 560px; top: 420px;
    width: 490px; height: 180px;
    background: var(--berry); color: var(--paper);
    display: flex; flex-direction: column; justify-content: center; align-items: center;
    font-size: 24px; line-height: 40px; font-weight: 400;
  }
</style>
</head>
<body>
  <article class="card">
    <section class="contact-panel">
      <span class="edge-tab edge-tab--upper"></span>
      <span class="edge-tab edge-tab--lower"></span>
      <h1 class="holder-name">Marcia Tolland, LMHC</h1>
      <p class="holder-company">Harbor Light Wellness &amp; Wellness Inc.</p>
      <ul class="contact-list">
        <li>Phone: 561-730-2254</li>
        <li>Fax: 561-730-2255</li>
        <li>Email: marcia@harborlightwa.example</li>
        <li>Website: www.harborlightwa.example</li>
      </ul>
    </section>
    <section class="brand-area">
      <span class="brand-mark"></span>
      <p class="brand-name">Harbor Light</p>
    </section>
    <address class="address-band" style="font-style:normal">
      <span>4823 W. Quarry Boulevard</span>
      <span>Suite 517, Boca Raton, FL 33412</span>
    </address>
  </article>
</body>
</html>
```